Website for The Pendry Parlour

I require a website for "The Pendry Parlour" which is a blog type business for 40+ year old women covering books, true crime, history, travel and food. It needs to support blog posts, links to social media including YouTube videos, Snapshelf, TikTok and Chatterpage. The background theme needs to be like that of a newspaper. Easy to navigate and to allow me to post blogs/videos.

```html
<!DOCTYPE html>
<html lang="en">
<head>
<meta charset="utf-8">
<title>The Pendry Parlour</title>
<link rel="stylesheet" href="https://fonts.googleapis.com/css2?family=Tinos&family=Poppins:wght@400;500&display=swap">
<style>
:root{
  --ink:#1a1a1a;
  --text:#333333;
  --rule:#bdbdbd;
  --paper:#ffffff;
  --tab:#ebebeb;
  --serif:"Tinos","Times New Roman",serif;
  --sans:"Poppins",Arial,sans-serif;
}
*{margin:0;padding:0;box-sizing:border-box}
html,body{width:1200px;height:4191px;overflow:hidden;background:var(--paper)}
body{position:relative;color:var(--ink);font-family:var(--sans)}
.abs{position:absolute}
.rule{position:absolute;left:109px;width:963px;height:1px;background:var(--rule)}
.serif{font-family:var(--serif)}
.meta{font-family:var(--serif);font-size:14px;top:30px}
.logo{font-family:var(--serif);font-size:44px;color:var(--ink);letter-spacing:-1px;line-height:1;white-space:nowrap}
.nav{top:92px;left:0;width:1200px;font-family:var(--serif);font-size:14.5px}
.nav a{position:absolute;color:var(--ink);text-decoration:none;white-space:nowrap}
.page-title{top:150px;left:109px;width:963px;text-align:center;font-family:var(--serif);font-size:46px;letter-spacing:9px}
.intro{top:226px;left:109px;width:963px;text-align:center;font-family:var(--serif);font-size:17.5px;line-height:24px;color:var(--text)}
.photo{position:absolute}
.body{font-size:12.5px;line-height:20.5px;color:var(--text);text-align:justify}
.more{font-family:var(--sans);font-weight:500;font-size:11.5px;color:var(--ink);text-decoration:underline;text-underline-offset:3px}
.headline{font-family:var(--serif);font-size:28px;line-height:34px;text-transform:uppercase;color:var(--ink)}
.tab{position:absolute;top:2096px;height:35px;background:var(--tab);font-family:var(--serif);font-size:17px;text-align:center;line-height:35px}
.news-title{font-family:var(--serif);font-size:27px;text-transform:uppercase;white-space:nowrap}
.page-box{position:absolute;top:3272px;width:32px;height:33px;border:1px solid var(--rule);font-family:var(--serif);font-size:17px;text-align:center;line-height:31px}
.foot-col{position:absolute;top:3958px;font-family:var(--serif);font-size:14px;line-height:23px}
.foot-col a{display:block;color:var(--ink);text-decoration:none;white-space:nowrap}
</style>
</head>
<body>

<header>
  <div class="abs meta" style="left:109px">8.00 PM</div>
  <div class="abs logo" style="left:0;width:1200px;text-align:center;top:14px">The Pendry Parlour</div>
  <div class="abs meta" style="right:128px">AUG 10,2025</div>
  <div class="rule" style="top:77px"></div>
  <nav class="abs nav">
    <a style="left:106px">HOME</a><a style="left:187px">BOOKS</a><a style="left:272px">TRUE CRIME</a><a style="left:379px">HISTORY</a><a style="left:470px">TRAVEL</a><a style="left:559px">FOOD</a><a style="left:631px">VIDEOS</a><a style="left:717px">ABOUT PENDRY</a><a style="left:867px">SUBSCRIBE</a><a style="left:979px">CONTACT</a>
  </nav>
  <div class="rule" style="top:125px"></div>
</header>

<main>
  <h1 class="abs page-title" style="font-weight:400">LORUM IPSUM DOLOR SIT AMET</h1>
  <div class="rule" style="top:210px"></div>
  <p class="abs intro">Lorem ipsum dolor sit amet, consectetur adipiscing elit, sed do eiusmod tempor incididunt ut labore et dolore magna aliqua. Ut enim ad minim veniam, quis nostrud exercitation ullamco laboris nisi ut aliquip ex ea commodo consequat. Duis aute irure dolor in reprehenderit in voluptate velit esse cillum dolore eu fugiat nulla pariatur.</p>

  <div class="photo" role="img" aria-label="Yellow crime scene tape across a rainy night street with a police car" style="left:109px;top:326px;width:672px;height:436px;background:radial-gradient(circle at 70% 35%,#7a6a3a,transparent 40%),linear-gradient(160deg,#3a3f44 0%,#1c1f22 55%,#5a4a12 80%,#1a1608 100%)"></div>
  <p class="abs body" style="left:811px;top:328px;width:260px;font-size:12.3px">Lorem ipsum dolor sit amet, consectetur adipiscing elit, sed do eiusmod tempor incididunt ut labore et dolore magna aliqua. Ut enim ad minim veniam, quis nostrud exercitation ullamco laboris nisi ut aliquip ex ea commodo consequat. Duis aute irure dolor in reprehenderit in voluptate velit esse cillum dolore eu fugiat nulla pariatur.Lorem ipsum dolor sit amet, consectetur adipiscing elit, sed do eiusmod tempor incididunt ut labore et dolore magna aliqua. Ut enim ad minim veniam, quis nostrud exercitation ullamco laboris nisi ut aliquip ex ea commodo consequat. Duis aute irure dolor in reprehenderit in voluptate velit esse cillum dolore eu fugiat nulla pariatur.Lorem ipsum dolor sit amet, consectetur adipiscing elit, sed do eiusmod tempor incididunt ut labore et dolore magna aliqua.</p>
  <p class="abs body" style="left:109px;top:781px;width:963px">Lorem ipsum dolor sit amet, consectetur adipiscing elit, sed do eiusmod tempor incididunt ut labore et dolore magna aliqua. Ut enim ad minim veniam, quis nostrud exercitation ullamco laboris nisi ut aliquip ex ea commodo consequat. Duis aute irure dolor in reprehenderit in voluptate velit esse cillum dolore eu fugiat nulla pariatur.Lorem ipsum dolor sit amet, consectetur adipiscing elit, sed do eiusmod tempor incididunt ut labore et dolore magna aliqua. Ut enim ad minim veniam, quis nostrud exercitation ullamco laboris nisi ut aliquip ex ea commodo consequat. Duis aute irure dolor in reprehenderit in voluptate velit esse cillum dolore eu fugiat nulla pariatur.Lorem ipsum dolor sit amet, consectetur adipiscing elit, sed do eiusmod tempor incididunt ut labore et dolore magna aliqua.</p>
  <div class="rule" style="top:931px"></div>

  <section class="cards">
    <div class="photo" role="img" aria-label="Woman standing on a riverside promenade with a city skyline" style="left:109px;top:965px;width:307px;height:213px;background:linear-gradient(180deg,#c9d3da 0%,#aeb7b8 55%,#8f8a7e 100%)"></div>
    <div class="photo" role="img" aria-label="Two business people walking up a flight of stairs" style="left:437px;top:965px;width:307px;height:213px;background:linear-gradient(180deg,#5d6468 0%,#8a8d8e 50%,#3d4145 100%)"></div>
    <div class="photo" role="img" aria-label="Hooded figure in a supermarket aisle" style="left:765px;top:965px;width:307px;height:213px;background:linear-gradient(120deg,#8fb4c8 0%,#4f7590 45%,#1e2f3e 100%)"></div>

    <p class="abs body" style="left:109px;top:1187px;width:307px">Lorem ipsum dolor sit amet, consectetur adipiscing elit, sed do eiusmod tempor incididunt ut labore et dolore magna aliqua. Ut enim ad minim veniam, quis nostrud exercitation ullamco laboris nisi ut aliquip ex ea commodo consequat.</p>
    <p class="abs body" style="left:437px;top:1187px;width:307px">Lorem ipsum dolor sit amet, consectetur adipiscing elit, sed do eiusmod tempor incididunt ut labore et dolore magna aliqua. Ut enim ad minim veniam, quis nostrud exercitation ullamco laboris nisi ut aliquip ex ea commodo consequat.</p>
    <p class="abs body" style="left:765px;top:1187px;width:307px">Lorem ipsum dolor sit amet, consectetur adipiscing elit, sed do eiusmod tempor incididunt ut labore et dolore magna aliqua. Ut enim ad minim veniam, quis nostrud exercitation ullamco laboris nisi ut aliquip ex ea commodo consequat.</p>
    <a class="abs more" style="left:111px;top:1325px">LEARN MORE</a>
    <a class="abs more" style="left:439px;top:1325px">LEARN MORE</a>
    <a class="abs more" style="left:767px;top:1325px">LEARN MORE</a>
  </section>
  <div class="rule" style="top:1382px"></div>

  <section class="feature">
    <h2 class="abs headline" style="left:109px;top:1418px;width:970px;font-weight:400">Lorem ipsum dolor sit amet, consectetur adipiscing elit, sed do eiusmod tempor incididunt ut labore et dolore</h2>
    <div class="photo" role="img" aria-label="Friends dancing at an outdoor party at dusk with string lights" style="left:109px;top:1498px;width:635px;height:392px;background:radial-gradient(circle at 40% 80%,#e6a45a,transparent 45%),linear-gradient(180deg,#8a98a6 0%,#b78a5e 50%,#6b4a2e 100%)"></div>
    <div class="photo" role="img" aria-label="Politician speaking to reporters holding microphones" style="left:765px;top:1498px;width:306px;height:222px;background:linear-gradient(160deg,#6c7682 0%,#3a4048 60%,#22262c 100%)"></div>
    <div class="photo" role="img" aria-label="Semicircular parliament chamber" style="left:765px;top:1744px;width:306px;height:195px;background:linear-gradient(180deg,#4a3a2a 0%,#7a5a3a 50%,#3a2a1c 100%)"></div>
    <p class="abs body" style="left:109px;top:1902px;width:635px">Lorem ipsum dolor sit amet, consectetur adipiscing elit, sed do eiusmod tempor incididunt ut labore et dolore magna aliqua. Ut enim ad minim veniam, quis nostrud exercitation ullamco laboris nisi ut aliquip ex ea commodo consequat. Duis aute irure dolor in reprehenderit</p>
    <a class="abs more" style="left:111px;top:1984px">LEARN MORE</a>
  </section>
  <div class="rule" style="top:2027px"></div>

  <section class="latest">
    <h2 class="abs serif" style="left:109px;top:2041px;font-size:28px;font-weight:400">LATEST NEWS</h2>
    <div class="tab" style="left:109px;width:150px">TRAVEL</div>
    <div class="tab" style="left:272px;width:147px">FOOD</div>
    <div class="tab" style="left:435px;width:147px">HISTORY</div>
    <div class="tab" style="left:598px;width:148px">CRIME</div>

    <article>
      <div class="photo" role="img" aria-label="Open book with reading glasses resting on it" style="left:109px;top:2162px;width:310px;height:248px;background:linear-gradient(150deg,#1a1714 0%,#5a4a36 55%,#c8b596 100%)"></div>
      <h3 class="abs news-title" style="left:449px;top:2190px;font-weight:400">Lorem ipsum dolor sit amet, consectetur</h3>
      <p class="abs body" style="left:449px;top:2240px;width:605px">Lorem ipsum dolor sit amet, consectetur adipiscing elit, sed do eiusmod tempor incididunt ut labore et dolore magna aliqua. Ut enim ad minim veniam, quis nostrud exercitation ullamco laboris nisi ut aliquip ex ea commodo consequat. Duis aute irure dolor in reprehenderit in voluptate velit esse cillum dolore eu fugiat nulla pariatur.Lorem ipsum dolor sit amet, consectetur adipiscing elit, sed do eiusmod tempor incididunt</p>
      <a class="abs more" style="left:450px;top:2364px">LEARN MORE</a>
    </article>
    <article>
      <div class="photo" role="img" aria-label="Ancient standing stones on green grass under a cloudy sky" style="left:109px;top:2432px;width:310px;height:248px;background:linear-gradient(180deg,#8f97a0 0%,#c2b9a8 40%,#4d5a3f 70%,#3e6b2a 100%)"></div>
      <h3 class="abs news-title" style="left:449px;top:2460px;font-weight:400">Lorem ipsum dolor sit amet, consectetur</h3>
      <p class="abs body" style="left:449px;top:2510px;width:605px">Lorem ipsum dolor sit amet, consectetur adipiscing elit, sed do eiusmod tempor incididunt ut labore et dolore magna aliqua. Ut enim ad minim veniam, quis nostrud exercitation ullamco laboris nisi ut aliquip ex ea commodo consequat. Duis aute irure dolor in reprehenderit in voluptate velit esse cillum dolore eu fugiat nulla pariatur.Lorem ipsum dolor sit amet, consectetur adipiscing elit, sed do eiusmod tempor incididunt</p>
      <a class="abs more" style="left:450px;top:2634px">LEARN MORE</a>
    </article>
    <article>
      <div class="photo" role="img" aria-label="Chef plating a dish with tweezers" style="left:109px;top:2702px;width:310px;height:248px;background:radial-gradient(circle at 45% 70%,#d9a255,transparent 40%),linear-gradient(160deg,#2b4a66 0%,#1d3348 60%,#3a2a22 100%)"></div>
      <h3 class="abs news-title" style="left:449px;top:2730px;font-weight:400">Lorem ipsum dolor sit amet, consectetur</h3>
      <p class="abs body" style="left:449px;top:2780px;width:605px">Lorem ipsum dolor sit amet, consectetur adipiscing elit, sed do eiusmod tempor incididunt ut labore et dolore magna aliqua. Ut enim ad minim veniam, quis nostrud exercitation ullamco laboris nisi ut aliquip ex ea commodo consequat. Duis aute irure dolor in reprehenderit in voluptate velit esse cillum dolore eu fugiat nulla pariatur.Lorem ipsum dolor sit amet, consectetur adipiscing elit, sed do eiusmod tempor incididunt</p>
      <a class="abs more" style="left:450px;top:2904px">LEARN MORE</a>
    </article>
    <article>
      <div class="photo" role="img" aria-label="Aerial view of a coastal cliffside town and turquoise sea" style="left:109px;top:2972px;width:310px;height:248px;background:linear-gradient(170deg,#8aa0a8 0%,#5e6b52 40%,#9a8f7c 60%,#1f6f78 100%)"></div>
      <h3 class="abs news-title" style="left:449px;top:3000px;font-weight:400">Lorem ipsum dolor sit amet, consectetur</h3>
      <p class="abs body" style="left:449px;top:3050px;width:605px">Lorem ipsum dolor sit amet, consectetur adipiscing elit, sed do eiusmod tempor incididunt ut labore et dolore magna aliqua. Ut enim ad minim veniam, quis nostrud exercitation ullamco laboris nisi ut aliquip ex ea commodo consequat. Duis aute irure dolor in reprehenderit in voluptate velit esse cillum dolore eu fugiat nulla pariatur.Lorem ipsum dolor sit amet, consectetur adipiscing elit, sed do eiusmod tempor incididunt</p>
      <a class="abs more" style="left:450px;top:3174px">LEARN MORE</a>
    </article>

    <nav class="pagination">
      <div class="page-box" style="left:429px">1</div>
      <div class="page-box" style="left:467px">2</div>
      <div class="page-box" style="left:506px">3</div>
      <div class="page-box" style="left:546px">4</div>
      <div class="abs serif" style="left:594px;top:3278px;font-size:17px">NEXT</div>
    </nav>
  </section>

  <div class="photo" role="img" aria-label="Row of social media post templates in purple and grey" style="left:109px;top:3376px;width:963px;height:299px;background:linear-gradient(90deg,#5a4f9a 0%,#5a4f9a 34%,#d9d9dc 34%,#d9d9dc 100%)"></div>

  <section class="blurb">
    <h2 class="abs serif" style="left:0;width:1200px;text-align:center;top:3733px;font-size:27px;font-weight:400">COME FOR THE BLOG, STAY FOR THE COMMENTS.</h2>
    <p class="abs body" style="left:288px;top:3780px;width:603px">Lorem ipsum dolor sit amet, consectetur adipiscing elit, sed do eiusmod tempor incididunt ut labore et dolore magna aliqua. Ut enim ad minim veniam, quis nostrud exercitation ullamco laboris nisi ut aliquip ex ea commodo consequat. Duis aute irure dolor in reprehenderit in voluptate velit esse cillum dolore eu fugiat nulla pariatur.Lorem ipsum dolor sit amet, <span style="display:block;text-align:center">consectetur adipiscing elit, sed do eiusmod tempor incididunt</span></p>
  </section>
</main>

<footer>
  <div class="rule" style="top:3923px"></div>
  <div class="abs logo" style="left:109px;top:3962px;font-size:42px">The Pendry Parlour</div>
  <div class="abs" style="left:111px;top:4030px;font-size:12.5px;color:var(--text)">Copyright@2025.All Rights Reserved</div>
  <div class="foot-col" style="left:558px"><a>HOME</a><a>BOOKS</a><a>TRUE CRIME HISTORY</a><a>TRAVEL</a></div>
  <div class="foot-col" style="left:787px"><a>FOOD</a><a>VIDEOS</a><a>ABOUT PENDRY</a><a>SUBSCRIBE</a><a>CONTACT</a></div>
  <div class="foot-col" style="left:982px"><a>CHATTERPAGE</a><a>SNAPSHELF</a><a>WORKLEDGER</a></div>
</footer>

</body>
</html>
```